Want a DL Flyer designed for mailout, with the following info. Please see the website www.ledgerwise.com.au for any other info.
Content:
EVERYTHING YOU NEED FROM AN ACCOUNTANT
(tick) Value for money
(tick) Mobile visits to your farm or business
(tick) Fixed Fees Agreed Upfront
(tick) Advice tailored to your circumstances
(tick) Help to grow your business
(tick) Talk directly to your accountant, the person who knows you
(tick) Small business & Primary Producer Specialists
+ MORE.......LEDGERWISE. YOU'RE MORE THAN A FILE TO US.
Director: Peter Dunmore CPA | Associate: Belinda Vasey CPA
Call (07) 4619 2235 www.ledgerwise.com.au PO Box 716 Marrowvale Qld 4630

```html
<!DOCTYPE html>
<html lang="en">
<head>
<meta charset="utf-8">
<title>Ledgerwise DL Flyer</title>
<link href="https://fonts.googleapis.com/css2?family=Source+Sans+3:wght@400;600;700;900&display=swap" rel="stylesheet">
<style>
  :root {
    --red: #e3202a;
    --ink: #1d1d1f;
    --grey: #8e9397;
    --grey-light: #e4e6e8;
    --grey-band: #c9cdd0;
    --stage: #8f8f8f;
    --paper: #ffffff;
  }
  * { box-sizing: border-box; margin: 0; padding: 0; }
  html, body { width: 738px; height: 1200px; overflow: hidden; }
  body {
    background: var(--stage);
    font-family: "Source Sans 3", "Source Sans Pro", sans-serif;
    color: var(--ink);
    position: relative;
  }
  .flyer {
    position: absolute;
    top: 250px;
    width: 330px;
    height: 700px;
    background: var(--paper);
    overflow: hidden;
    box-shadow: 0 6px 18px rgba(0,0,0,.25);
  }
  .flyer--front { left: 26px; }
  .flyer--back { left: 382px; background: linear-gradient(180deg, #fff 0%, #f1f2f3 45%, #e6e7e8 75%, #fff 76%); }

  .brand {
    position: absolute; left: 0; right: 0;
    display: flex; align-items: center; justify-content: center; gap: 8px;
    font-weight: 700; color: var(--red); letter-spacing: .5px;
  }
  .brand__mark { width: 14px; height: 14px; background: var(--red); }
  .flyer--front .brand { top: 76px; font-size: 26px; }
  .flyer--back .brand { top: 358px; font-size: 22px; }

  .front__rule { position: absolute; top: 130px; left: 0; right: 0; height: 5px; background: var(--red); }
  .front__photo {
    position: absolute; top: 135px; left: 0; right: 0; height: 230px;
    background: linear-gradient(160deg, #2b2f36 0%, #6b7076 35%, #b9b2a8 65%, #8a7a66 100%);
  }
  .front__swoosh { position: absolute; top: 300px; left: 0; width: 330px; height: 120px; }
  .front__headline {
    position: absolute; top: 420px; left: 24px;
    font-size: 38px; line-height: 39px; font-weight: 400;
  }
  .front__headline strong { font-weight: 900; color: var(--red); }
  .front__headline .red { color: var(--red); }
  .front__bar { position: absolute; top: 549px; left: 24px; width: 190px; height: 6px; background: var(--ink); }
  .front__copy { position: absolute; top: 582px; left: 24px; right: 18px; font-size: 11.5px; line-height: 16px; }
  .front__copy em { font-style: normal; color: var(--red); }
  .front__band {
    position: absolute; bottom: 0; left: 0; right: 0; height: 54px;
    background: linear-gradient(90deg, var(--grey-band), var(--grey-light) 50%, var(--grey-band));
    display: flex; align-items: center; justify-content: center;
    color: var(--red); font-weight: 600; font-size: 12px;
  }

  .back__photo {
    position: absolute; top: 0; right: 0; width: 150px; height: 140px;
    background: linear-gradient(225deg, #cfd1d3 0%, #eceded 60%, rgba(255,255,255,0) 100%);
  }
  .back__title {
    position: absolute; top: 34px; left: 24px;
    color: var(--red); font-weight: 700; font-size: 15px; line-height: 16px;
  }
  .back__title-rule { position: absolute; top: 72px; left: 24px; width: 120px; height: 3px; background: var(--ink); }
  .checklist { position: absolute; top: 102px; left: 24px; right: 20px; list-style: none; }
  .checklist li {
    position: relative; padding-left: 16px; font-size: 11px; line-height: 13px; margin-bottom: 10px;
  }
  .checklist svg { position: absolute; left: 0; top: 1px; width: 10px; height: 10px; }
  .back__more { position: absolute; top: 284px; left: 30px; color: var(--red); font-size: 12px; font-weight: 600; }
  .back__headline {
    position: absolute; top: 422px; left: 30px;
    font-size: 28px; line-height: 30px; font-weight: 400;
  }
  .back__headline .red { color: var(--red); }
  .back__headline strong { font-weight: 900; }
  .back__swoosh { position: absolute; top: 490px; left: 0; width: 330px; height: 60px; }
  .back__portrait {
    position: absolute; top: 526px; right: 20px; width: 128px; height: 130px;
    border: 4px solid #9ea2a5;
    background: linear-gradient(180deg, #3f5a3a 0%, #6e8a5a 45%, #9fb3cc 100%);
  }
  .back__team {
    position: absolute; top: 556px; left: 0; width: 184px; height: 32px;
    background: #1f1f1f; color: #fff; font-size: 9.5px; font-weight: 600; line-height: 12px;
    padding: 4px 0 0 24px;
  }
  .contacts { position: absolute; top: 600px; left: 24px; list-style: none; }
  .contacts li { display: flex; align-items: center; gap: 7px; font-size: 9.5px; margin-bottom: 8px; }
  .contacts svg { width: 10px; height: 10px; }
  .back__base { position: absolute; bottom: 0; left: 0; right: 0; height: 14px; background: var(--red); }
</style>
</head>
<body>

<section class="flyer flyer--front">
  <div class="brand"><span class="brand__mark"></span>LEDGERWISE</div>
  <div class="front__rule"></div>
  <div class="front__photo" role="img" aria-label="Photo of two business people shaking hands across a desk with a laptop and documents"></div>
  <svg class="front__swoosh" viewBox="0 0 330 120" preserveAspectRatio="none" aria-hidden="true">
    <path d="M0 38 Q170 -10 330 78 L330 120 L0 120 Z" fill="#e3202a"/>
    <path d="M0 50 Q180 4 330 108 L330 120 L0 120 Z" fill="#ffffff"/>
  </svg>
  <h1 class="front__headline"><strong>YOU</strong> are <strong>NOT</strong><br>just a number<br><span class="red">with <strong>US</strong></span></h1>
  <div class="front__bar"></div>
  <p class="front__copy">If you are looking for a personalised service for you and your business - call us on <em>07 4619 2235</em> or <em>0412 555 318</em> and experience the difference today</p>
  <div class="front__band">www.ledgerwise.com.au</div>
</section>

<section class="flyer flyer--back">
  <div class="back__photo" role="img" aria-label="Faded photo of an accountant writing at a desk"></div>
  <h2 class="back__title">EVERYTHING YOU NEED<br>FROM AN ACCOUNTANT</h2>
  <div class="back__title-rule"></div>
  <ul class="checklist">
    <li><svg viewBox="0 0 10 10"><circle cx="5" cy="5" r="4.2" fill="none" stroke="#e3202a" stroke-width="1"/><path d="M3 5.2 L4.5 6.7 L8.5 2" fill="none" stroke="#1d1d1f" stroke-width="1.3"/></svg>Value for money</li>
    <li><svg viewBox="0 0 10 10"><circle cx="5" cy="5" r="4.2" fill="none" stroke="#e3202a" stroke-width="1"/><path d="M3 5.2 L4.5 6.7 L8.5 2" fill="none" stroke="#1d1d1f" stroke-width="1.3"/></svg>Mobile visits to your farm or business</li>
    <li><svg viewBox="0 0 10 10"><circle cx="5" cy="5" r="4.2" fill="none" stroke="#e3202a" stroke-width="1"/><path d="M3 5.2 L4.5 6.7 L8.5 2" fill="none" stroke="#1d1d1f" stroke-width="1.3"/></svg>Fixed Fees Agreed Upfront</li>
    <li><svg viewBox="0 0 10 10"><circle cx="5" cy="5" r="4.2" fill="none" stroke="#e3202a" stroke-width="1"/><path d="M3 5.2 L4.5 6.7 L8.5 2" fill="none" stroke="#1d1d1f" stroke-width="1.3"/></svg>Advice tailored to your circumstances</li>
    <li><svg viewBox="0 0 10 10"><circle cx="5" cy="5" r="4.2" fill="none" stroke="#e3202a" stroke-width="1"/><path d="M3 5.2 L4.5 6.7 L8.5 2" fill="none" stroke="#1d1d1f" stroke-width="1.3"/></svg>Help to grow your business</li>
    <li><svg viewBox="0 0 10 10"><circle cx="5" cy="5" r="4.2" fill="none" stroke="#e3202a" stroke-width="1"/><path d="M3 5.2 L4.5 6.7 L8.5 2" fill="none" stroke="#1d1d1f" stroke-width="1.3"/></svg>Talk directly to your accountant,<br>the person who knows you</li>
    <li><svg viewBox="0 0 10 10"><circle cx="5" cy="5" r="4.2" fill="none" stroke="#e3202a" stroke-width="1"/><path d="M3 5.2 L4.5 6.7 L8.5 2" fill="none" stroke="#1d1d1f" stroke-width="1.3"/></svg>Small business &amp; Primary Producer Specialists</li>
  </ul>
  <div class="back__more">+ MORE.......</div>
  <div class="brand"><span class="brand__mark"></span>LEDGERWISE</div>
  <h2 class="back__headline"><span class="red">YOU'RE <strong>MORE</strong></span> THAN<br>A FILE <span class="red">TO <strong>US.</strong></span></h2>
  <svg class="back__swoosh" viewBox="0 0 330 60" preserveAspectRatio="none" aria-hidden="true">
    <path d="M0 30 Q160 -6 330 40 L330 60 Q160 10 0 40 Z" fill="#8e9397"/>
    <path d="M0 40 Q160 10 330 60 L0 60 Z" fill="#ffffff"/>
  </svg>
  <div class="back__portrait" role="img" aria-label="Portrait photo of the director outdoors in front of trees"></div>
  <div class="back__team">Director: Peter Dunmore CPA |<br>Associate: Belinda Vasey CPA</div>
  <ul class="contacts">
    <li><svg viewBox="0 0 10 10"><path d="M1 5 L5 1.5 L9 5 M2.5 4 V9 H7.5 V4" fill="none" stroke="#e3202a" stroke-width="1"/></svg>PO Box 716 Marrowvale Qld 4630</li>
    <li><svg viewBox="0 0 10 10"><path d="M2 1.5 L3.8 1.5 L4.5 3.5 L3.4 4.3 Q4.5 6.2 5.8 6.7 L6.6 5.6 L8.5 6.3 L8.5 8.2 Q4 8.5 1.6 3 Z" fill="none" stroke="#e3202a" stroke-width="1"/></svg>Call (07) 4619 2235</li>
    <li><svg viewBox="0 0 10 10"><circle cx="5" cy="5" r="4" fill="none" stroke="#e3202a" stroke-width="1"/><path d="M1 5 H9 M5 1 Q2.5 5 5 9 M5 1 Q7.5 5 5 9" fill="none" stroke="#e3202a" stroke-width=".8"/></svg>www.ledgerwise.com.au</li>
  </ul>
  <div class="back__base"></div>
</section>

</body>
</html>
```